Golf app new design

New design of a golf app. The app enables customers to book tee time, measure each other and win prizes. 5 screens are to be designed. The app should look high-quality, calm and elegant.

```html
<!DOCTYPE html>
<html lang="en">
<head>
<meta charset="utf-8">
<title>Teeline – Golf App Screens</title>
<link href="https://fonts.googleapis.com/css2?family=Poppins:wght@400;500;600;700&display=swap" rel="stylesheet">
<style>
:root{
  --bg:#ebe8e4;
  --white:#ffffff;
  --green:#6cc224;
  --green-soft:#d7efc2;
  --ink:#2f3133;
  --grey:#8d9092;
  --line:#e6e7e8;
  --card-dark:#626464;
  --card-dark-2:#4f5151;
  --star:#f2c12e;
}
*{box-sizing:border-box;margin:0;padding:0}
html,body{width:1200px;height:608px;overflow:hidden}
body{background:var(--bg);font-family:'Poppins',sans-serif;color:var(--ink);position:relative}

.screen{position:absolute;background:var(--white);border-radius:18px;overflow:hidden;box-shadow:0 14px 34px rgba(60,55,50,.12)}
.screen--home{left:488px;top:58px;width:224px;height:492px;z-index:3;padding:0 14px}
.screen--profile{top:90px;width:180px;height:430px;z-index:2;padding:0 12px}
.screen--profile.is-left{left:290px}
.screen--profile.is-right{left:730px}
.screen--ranking{top:130px;width:150px;height:360px;z-index:1}
.screen--ranking.is-left{left:150px}
.screen--ranking.is-right{left:900px}

.topbar{height:42px;display:flex;align-items:center;justify-content:space-between}
.burger{width:14px;display:flex;flex-direction:column;gap:3px}
.burger i{display:block;height:1.6px;background:var(--ink);border-radius:1px}
.brand{font-weight:700;color:var(--green);font-size:15px;letter-spacing:-.3px}

/* home */
.greet{display:flex;align-items:center;margin-top:6px}
.avatar{border-radius:50%;background:linear-gradient(150deg,#c9b8a6,#7d6a5c);flex:none}
.greet .avatar{width:30px;height:30px}
.greet-text{margin-left:8px;flex:1}
.greet-text b{display:block;font-size:12px;font-weight:600}
.greet-text span{font-size:6px;color:var(--grey)}
.stats{display:flex;align-items:center;gap:8px}
.stat{text-align:center}
.stat b{display:block;color:var(--green);font-size:10px;font-weight:600;line-height:1.1}
.stat span{font-size:5px;color:var(--grey)}
.stat-divider{width:1px;height:18px;background:var(--line)}

.contest{margin-top:16px;height:110px;border-radius:6px;background:linear-gradient(120deg,#7a7c7c,var(--card-dark-2));position:relative;color:var(--white)}
.contest h2{position:absolute;left:14px;top:26px;width:92px;font-size:13px;line-height:1.35;font-weight:600}
.contest .amount{position:absolute;right:16px;top:24px;text-align:right}
.contest .amount b{display:block;color:var(--green);font-size:13px;font-weight:600}
.contest .amount span{font-size:6.5px}
.contest svg{position:absolute;left:30px;top:52px}

.tiles{display:flex;gap:8px;margin-top:14px}
.tile{flex:1;height:48px;border-radius:3px;box-shadow:0 3px 10px rgba(0,0,0,.08);display:flex;flex-direction:column;align-items:center;justify-content:center;gap:5px}
.tile span{font-size:6px;color:var(--green);text-decoration:underline}

.section-head{display:flex;align-items:center;justify-content:space-between;margin-top:16px}
.section-head h3{font-size:11px;font-weight:600;display:flex;align-items:center;gap:5px}
.section-head a{font-size:5.5px;color:var(--green);text-decoration:none}

.prize{display:flex;gap:8px;align-items:center;padding:7px 8px;margin-top:8px;box-shadow:0 3px 10px rgba(0,0,0,.08);border-radius:2px}
.prize-photo{width:38px;height:28px;flex:none;background:linear-gradient(160deg,#a8d88a,#4f8f37)}
.prize b{display:block;font-size:7.5px;font-weight:600}
.prize p{font-size:5.5px;color:var(--grey);line-height:1.4}

.nav{position:absolute;left:0;right:0;bottom:0;height:40px;background:var(--white);box-shadow:0 -3px 10px rgba(0,0,0,.05);display:flex;align-items:center;justify-content:space-around;padding:0 8px}
.nav-active{display:flex;align-items:center;gap:3px;background:var(--green-soft);color:var(--green);border-radius:3px;padding:4px 7px;font-size:6px;font-weight:500}
.nav svg{display:block}

/* profile */
.screen--profile .topbar{height:38px;position:relative}
.page-title{position:absolute;left:0;right:0;text-align:center;font-size:9px;color:var(--ink);pointer-events:none}
.profile-photo{width:66px;height:66px;margin:8px auto 0;border-radius:50%;background:var(--green-soft);padding:5px}
.profile-photo .avatar{width:100%;height:100%}
.profile-name{text-align:center;font-size:10px;font-weight:600;margin-top:8px}
.profile-sub{text-align:center;font-size:5px;color:var(--grey)}
.profile-stats{display:flex;align-items:center;justify-content:space-between;margin-top:18px;padding:0 8px}
.btn-edit{background:#4a4c4c;color:var(--white);font-size:5.5px;border-radius:8px;padding:3px 9px}
.friends{margin-top:18px}
.friends h3{font-size:11px;font-weight:600;color:#555}
.friends p{font-size:5.5px;color:var(--grey)}
.friend-row{display:flex;margin-top:8px}
.friend-row > *{width:16px;height:16px;border-radius:50%;border:1.5px solid var(--white);margin-right:-4px;flex:none}
.friend-add{background:#8a8c8c;display:flex;align-items:center;justify-content:center}
.friend-more{background:var(--green);color:var(--white);font-size:5px;display:flex;align-items:center;justify-content:center}
.sync{margin-top:18px;background:linear-gradient(120deg,var(--card-dark),var(--card-dark-2));border-radius:4px;padding:10px 14px 12px;color:var(--white)}
.sync h4{font-size:7.5px;font-weight:600;text-align:center;line-height:1.35}
.field{display:flex;align-items:center;gap:4px;border-bottom:1px solid rgba(255,255,255,.6);padding:6px 0 3px;font-size:5px;color:rgba(255,255,255,.8)}
.btn-save{display:block;width:40px;margin:10px auto 0;background:var(--green);color:var(--white);font-size:5.5px;text-align:center;padding:2px 0;border-radius:1px}

/* ranking */
.rank-hero{height:128px;background:linear-gradient(180deg,#e6f3d9 0%,#a8d98a 55%,#7fbf5a 100%);position:relative;padding:0 10px}
.rank-hero .topbar{height:34px}
.rank-hero .brand{font-size:11px}
.rank-hero h2{position:absolute;left:10px;top:60px;width:70px;font-size:10px;line-height:1.3;color:var(--white);font-weight:600}
.rank-hero .max{position:absolute;right:10px;top:72px;font-size:5px;color:var(--white)}
.rank-badge{position:absolute;right:10px;top:96px;width:44px;height:44px;border-radius:50%;background:var(--green);border:3px solid var(--white);color:var(--white);text-align:center;padding-top:6px}
.rank-badge span{display:block;font-size:4px}
.rank-badge b{display:block;font-size:17px;font-weight:700;line-height:1.1}
.rank-list{padding:30px 10px 0}
.rank-row{display:flex;align-items:center;gap:4px;height:22px;padding:0 6px;margin-bottom:9px;box-shadow:0 2px 8px rgba(0,0,0,.08);border-radius:2px;font-size:5px}
.rank-row .avatar{width:8px;height:8px}
.rank-row .user{flex:1;color:var(--grey)}
.rank-row .prize-amount{font-size:5.5px;font-weight:600}
.screen--ranking .nav{height:30px}
</style>
</head>
<body>

<!-- Ranking screens -->
<section class="screen screen--ranking is-left">
  <div class="rank-hero" role="img" aria-label="Photo of a golfer swinging on a sunny fairway">
    <div class="topbar"><div class="burger"><i></i><i></i><i></i></div><span class="brand">Teeline</span></div>
    <h2>Virtual Golf Ranking</h2>
    <span class="max">Max 10</span>
    <div class="rank-badge"><span>Your rank</span><b>5</b></div>
  </div>
  <div class="rank-list">
    <div class="rank-row"><span>#1</span><span class="avatar"></span><span class="user">username</span><span class="prize-amount">$7900</span></div>
    <div class="rank-row"><span>#2</span><span class="avatar"></span><span class="user">username</span><span class="prize-amount">$7900</span></div>
    <div class="rank-row"><span>#3</span><span class="avatar"></span><span class="user">username</span><span class="prize-amount">$7900</span></div>
    <div class="rank-row"><span>#4</span><span class="avatar"></span><span class="user">username</span><span class="prize-amount">$7900</span></div>
  </div>
  <nav class="nav">
    <svg width="8" height="8" viewBox="0 0 16 16"><path d="M2 8 8 2l6 6v6H2z" fill="#9a9d9f"/></svg>
    <span class="nav-active"><svg width="7" height="7" viewBox="0 0 16 16"><path d="M2 14V8h3v6zm4.5 0V3h3v11zM11 14V6h3v8z" fill="#6cc224"/></svg>Ranking</span>
    <svg width="8" height="8" viewBox="0 0 16 16"><rect x="1" y="4" width="14" height="10" rx="2" fill="#9a9d9f"/><circle cx="8" cy="9" r="3" fill="#fff"/></svg>
    <svg width="8" height="8" viewBox="0 0 16 16"><circle cx="8" cy="8" r="7" fill="#9a9d9f"/><path d="M8 4v4l3 2" stroke="#fff" stroke-width="1.6" fill="none"/></svg>
    <svg width="8" height="8" viewBox="0 0 16 16"><circle cx="8" cy="5" r="3.5" fill="#9a9d9f"/><path d="M1.5 15c0-4 3-6 6.5-6s6.5 2 6.5 6z" fill="#9a9d9f"/></svg>
  </nav>
</section>

<section class="screen screen--ranking is-right">
  <div class="rank-hero" role="img" aria-label="Photo of a golfer swinging on a sunny fairway">
    <div class="topbar"><div class="burger"><i></i><i></i><i></i></div><span class="brand">Teeline</span></div>
    <h2>Virtual Golf Ranking</h2>
    <span class="max">Max 10</span>
    <div class="rank-badge"><span>Your rank</span><b>5</b></div>
  </div>
  <div class="rank-list">
    <div class="rank-row"><span>#1</span><span class="avatar"></span><span class="user">username</span><span class="prize-amount">$7900</span></div>
    <div class="rank-row"><span>#2</span><span class="avatar"></span><span class="user">username</span><span class="prize-amount">$7900</span></div>
    <div class="rank-row"><span>#3</span><span class="avatar"></span><span class="user">username</span><span class="prize-amount">$7900</span></div>
    <div class="rank-row"><span>#4</span><span class="avatar"></span><span class="user">username</span><span class="prize-amount">$7900</span></div>
  </div>
  <nav class="nav">
    <svg width="8" height="8" viewBox="0 0 16 16"><path d="M2 8 8 2l6 6v6H2z" fill="#9a9d9f"/></svg>
    <span class="nav-active"><svg width="7" height="7" viewBox="0 0 16 16"><path d="M2 14V8h3v6zm4.5 0V3h3v11zM11 14V6h3v8z" fill="#6cc224"/></svg>Ranking</span>
    <svg width="8" height="8" viewBox="0 0 16 16"><rect x="1" y="4" width="14" height="10" rx="2" fill="#9a9d9f"/><circle cx="8" cy="9" r="3" fill="#fff"/></svg>
    <svg width="8" height="8" viewBox="0 0 16 16"><circle cx="8" cy="8" r="7" fill="#9a9d9f"/><path d="M8 4v4l3 2" stroke="#fff" stroke-width="1.6" fill="none"/></svg>
    <svg width="8" height="8" viewBox="0 0 16 16"><circle cx="8" cy="5" r="3.5" fill="#9a9d9f"/><path d="M1.5 15c0-4 3-6 6.5-6s6.5 2 6.5 6z" fill="#9a9d9f"/></svg>
  </nav>
</section>

<!-- Profile screens -->
<section class="screen screen--profile is-left">
  <div class="topbar"><div class="burger"><i></i><i></i><i></i></div><span class="page-title">Profile</span><span></span></div>
  <div class="profile-photo"><div class="avatar" role="img" aria-label="Profile photo of the player"></div></div>
  <p class="profile-name">Owen Hartley</p>
  <p class="profile-sub">Pro golfer, 12 hcp</p>
  <div class="profile-stats">
    <div class="stat"><b>124</b><span>Points</span></div>
    <span class="btn-edit">Edit Profile</span>
    <div class="stat"><b>#1</b><span>Ranking</span></div>
  </div>
  <div class="friends">
    <h3>Friends</h3>
    <p>Recently People Added</p>
    <div class="friend-row">
      <span class="friend-add"><svg width="7" height="7" viewBox="0 0 10 10"><path d="M5 1v8M1 5h8" stroke="#fff" stroke-width="1.6"/></svg></span>
      <span class="avatar"></span><span class="avatar"></span><span class="avatar"></span>
      <span class="friend-more">+5</span>
    </div>
  </div>
  <div class="sync">
    <h4>To Import Friend Synchronise with ClubSync</h4>
    <div class="field"><svg width="6" height="6" viewBox="0 0 16 16"><circle cx="8" cy="5" r="3.5" fill="#6cc224"/><path d="M1.5 15c0-4 3-6 6.5-6s6.5 2 6.5 6z" fill="#6cc224"/></svg>Enter your username</div>
    <div class="field"><svg width="6" height="6" viewBox="0 0 16 16"><rect x="3" y="7" width="10" height="8" rx="1" fill="#6cc224"/><path d="M5 7V5a3 3 0 0 1 6 0v2" stroke="#6cc224" stroke-width="1.6" fill="none"/></svg>Password</div>
    <span class="btn-save">Save</span>
  </div>
  <nav class="nav">
    <svg width="9" height="9" viewBox="0 0 16 16"><path d="M2 8 8 2l6 6v6H2z" fill="#9a9d9f"/></svg>
    <svg width="9" height="9" viewBox="0 0 16 16"><path d="M2 14V8h3v6zm4.5 0V3h3v11zM11 14V6h3v8z" fill="#9a9d9f"/></svg>
    <svg width="9" height="9" viewBox="0 0 16 16"><rect x="1" y="4" width="14" height="10" rx="2" fill="#9a9d9f"/><circle cx="8" cy="9" r="3" fill="#fff"/></svg>
    <svg width="9" height="9" viewBox="0 0 16 16"><circle cx="8" cy="8" r="7" fill="#9a9d9f"/><path d="M8 4v4l3 2" stroke="#fff" stroke-width="1.6" fill="none"/></svg>
    <span class="nav-active"><svg width="7" height="7" viewBox="0 0 16 16"><circle cx="8" cy="5" r="3.5" fill="#6cc224"/><path d="M1.5 15c0-4 3-6 6.5-6s6.5 2 6.5 6z" fill="#6cc224"/></svg>Profile</span>
  </nav>
</section>

<section class="screen screen--profile is-right">
  <div class="topbar"><div class="burger"><i></i><i></i><i></i></div><span class="page-title">Profile</span><span></span></div>
  <div class="profile-photo"><div class="avatar" role="img" aria-label="Profile photo of the player"></div></div>
  <p class="profile-name">Owen Hartley</p>
  <p class="profile-sub">Pro golfer, 12 hcp</p>
  <div class="profile-stats">
    <div class="stat"><b>124</b><span>Points</span></div>
    <span class="btn-edit">Edit Profile</span>
    <div class="stat"><b>#1</b><span>Ranking</span></div>
  </div>
  <div class="friends">
    <h3>Friends</h3>
    <p>Recently People Added</p>
    <div class="friend-row">
      <span class="friend-add"><svg width="7" height="7" viewBox="0 0 10 10"><path d="M5 1v8M1 5h8" stroke="#fff" stroke-width="1.6"/></svg></span>
      <span class="avatar"></span><span class="avatar"></span><span class="avatar"></span>
      <span class="friend-more">+5</span>
    </div>
  </div>
  <div class="sync">
    <h4>To Import Friend Synchronise with ClubSync</h4>
    <div class="field"><svg width="6" height="6" viewBox="0 0 16 16"><circle cx="8" cy="5" r="3.5" fill="#6cc224"/><path d="M1.5 15c0-4 3-6 6.5-6s6.5 2 6.5 6z" fill="#6cc224"/></svg>Enter your username</div>
    <div class="field"><svg width="6" height="6" viewBox="0 0 16 16"><rect x="3" y="7" width="10" height="8" rx="1" fill="#6cc224"/><path d="M5 7V5a3 3 0 0 1 6 0v2" stroke="#6cc224" stroke-width="1.6" fill="none"/></svg>Password</div>
    <span class="btn-save">Save</span>
  </div>
  <nav class="nav">
    <svg width="9" height="9" viewBox="0 0 16 16"><path d="M2 8 8 2l6 6v6H2z" fill="#9a9d9f"/></svg>
    <svg width="9" height="9" viewBox="0 0 16 16"><path d="M2 14V8h3v6zm4.5 0V3h3v11zM11 14V6h3v8z" fill="#9a9d9f"/></svg>
    <svg width="9" height="9" viewBox="0 0 16 16"><rect x="1" y="4" width="14" height="10" rx="2" fill="#9a9d9f"/><circle cx="8" cy="9" r="3" fill="#fff"/></svg>
    <svg width="9" height="9" viewBox="0 0 16 16"><circle cx="8" cy="8" r="7" fill="#9a9d9f"/><path d="M8 4v4l3 2" stroke="#fff" stroke-width="1.6" fill="none"/></svg>
    <span class="nav-active"><svg width="7" height="7" viewBox="0 0 16 16"><circle cx="8" cy="5" r="3.5" fill="#6cc224"/><path d="M1.5 15c0-4 3-6 6.5-6s6.5 2 6.5 6z" fill="#6cc224"/></svg>Profile</span>
  </nav>
</section>

<!-- Home screen -->
<section class="screen screen--home">
  <div class="topbar"><div class="burger"><i></i><i></i><i></i></div><span class="brand">Teeline</span></div>
  <div class="greet">
    <div class="avatar" role="img" aria-label="Small profile photo of the player"></div>
    <div class="greet-text"><b>Hi There,</b><span>Welcome back</span></div>
    <div class="stats">
      <div class="stat"><b>124</b><span>Points</span></div>
      <span class="stat-divider"></span>
      <div class="stat"><b>#1</b><span>Ranking</span></div>
    </div>
  </div>
  <div class="contest">
    <h2>Winning The Contest</h2>
    <div class="amount"><b>$2300</b><span>12-14 Nov</span></div>
    <svg width="140" height="50" viewBox="0 0 140 50"><path d="M2 46 C50 46 90 30 124 6" stroke="#fff" stroke-width="2" fill="none" stroke-linecap="round"/><circle cx="124" cy="6" r="3.5" fill="#fff"/></svg>
  </div>
  <div class="tiles">
    <div class="tile"><svg width="18" height="16" viewBox="0 0 18 16"><circle cx="7" cy="5" r="3.5" fill="#8d9092"/><path d="M0.5 15c0-4 3-6 6.5-6s6.5 2 6.5 6z" fill="#8d9092"/><path d="M15 4v6M12 7h6" stroke="#8d9092" stroke-width="1.6"/></svg><span>Leaderboards</span></div>
    <div class="tile"><svg width="16" height="16" viewBox="0 0 16 16"><circle cx="8" cy="8" r="7" fill="none" stroke="#3b8ed6" stroke-width="1.4"/><path d="M4.5 6.5h7l-2-2M11.5 9.5h-7l2 2" stroke="#3b8ed6" stroke-width="1.3" fill="none"/></svg><span>How it works</span></div>
    <div class="tile"><svg width="16" height="16" viewBox="0 0 16 16"><path d="M4 1h8v5a4 4 0 0 1-8 0z" fill="#f2c12e"/><path d="M4 3H1.5a2.5 2.5 0 0 0 2.8 3M12 3h2.5a2.5 2.5 0 0 1-2.8 3" stroke="#f2c12e" stroke-width="1.2" fill="none"/><rect x="7" y="10" width="2" height="3" fill="#f2c12e"/><rect x="5" y="13" width="6" height="2" fill="#f2c12e"/></svg><span>Prizes</span></div>
  </div>
  <div class="section-head">
    <h3><svg width="11" height="11" viewBox="0 0 16 16"><path d="M8 1l2.1 4.5 4.9.6-3.6 3.4.9 4.9L8 12l-4.3 2.4.9-4.9L1 6.1l4.9-.6z" fill="#f2c12e"/></svg>Prizes</h3>
    <a href="#">See All</a>
  </div>
  <div class="prize"><div class="prize-photo" role="img" aria-label="Photo of a golf prize on the green"></div><div><b>Lorem Ipsum</b><p>A simply dummy text of the printing and typesetting industry.</p></div></div>
  <div class="prize"><div class="prize-photo" role="img" aria-label="Photo of a golf prize on the green"></div><div><b>Lorem Ipsum</b><p>A simply dummy text of the printing and typesetting industry.</p></div></div>
  <div class="prize"><div class="prize-photo" role="img" aria-label="Photo of a golf prize on the green"></div><div><b>Lorem Ipsum</b><p>A simply dummy text of the printing and typesetting industry.</p></div></div>
  <nav class="nav">
    <span class="nav-active"><svg width="8" height="8" viewBox="0 0 16 16"><path d="M2 8 8 2l6 6v6H2z" fill="#6cc224"/></svg>Home</span>
    <svg width="10" height="10" viewBox="0 0 16 16"><path d="M2 14V8h3v6zm4.5 0V3h3v11zM11 14V6h3v8z" fill="#9a9d9f"/></svg>
    <svg width="10" height="10" viewBox="0 0 16 16"><rect x="1" y="4" width="14" height="10" rx="2" fill="#9a9d9f"/><circle cx="8" cy="9" r="3" fill="#fff"/></svg>
    <svg width="10" height="10" viewBox="0 0 16 16"><circle cx="8" cy="8" r="7" fill="#9a9d9f"/><path d="M8 4v4l3 2" stroke="#fff" stroke-width="1.6" fill="none"/></svg>
    <svg width="10" height="10" viewBox="0 0 16 16"><circle cx="8" cy="5" r="3.5" fill="#9a9d9f"/><path d="M1.5 15c0-4 3-6 6.5-6s6.5 2 6.5 6z" fill="#9a9d9f"/></svg>
  </nav>
</section>

</body>
</html>
```